Upsell Vertical Banner Ad Design For B2B Marketing Agency Vertical 768px × 1180px IS THE SIZE

I need a banner made for my website www.brightlanepromotionhub.biz This banner will be an upsell advertisement for after someone signs up for my monthly program. When they login to their account for the 1st time I will give them the chance to upgrade their account to our annual program with just one click.

this is a page that upsells it currently to give you an idea how we market ourselves:
https://tlpx.pagevault-example.com/page/tlp-annual-upsell

Use this content:

Are You Ready To Commit To Taking Your Business To The Next Level?

Because We're In This For The Long-Haul and Dedicated To Your Success...

Save $300 By Upgrading To An Annual Membership And Pay Only $74/mth

((BUTTON))Yes, Upgrade My Plan Right Now!

*Must prepay the full year at only $898/yr!

Target Market(s)

business owners

Industry/Entity Type

Marketing

Requirements
Must have
• 768px × 1180px IS THE SIZE vertical

Use this content:

Nice to have
• Use this content:

Should not have
• Use this content:

```html
<!DOCTYPE html>
<html lang="en">
<head>
<meta charset="utf-8">
<title>Brightlane Promotion Hub – Annual Upgrade</title>
<link href="https://fonts.googleapis.com/css2?family=Poppins:wght@500;600;700;800&display=swap" rel="stylesheet">
<style>
  :root {
    --bg-top: #e4eef6;
    --bg-bottom: #cfe0ed;
    --ink: #111418;
    --brand: #1f6fb5;
    --frame: #2b86d6;
    --button: #3fd24c;
    --button-shadow: #2fa93a;
    --white: #ffffff;
    --photo-light: #d5dde4;
    --photo-mid: #7c8aa0;
    --photo-dark: #23355c;
  }
  * { margin: 0; padding: 0; box-sizing: border-box; }
  html, body { width: 783px; height: 1200px; overflow: hidden; }
  body {
    font-family: "Poppins", Arial, sans-serif;
    color: var(--ink);
    background: linear-gradient(180deg, var(--bg-top), var(--bg-bottom));
  }
  .banner {
    position: relative;
    width: 783px;
    height: 1200px;
    text-align: center;
  }
  .brand {
    position: absolute;
    top: 34px;
    left: 0; right: 0;
    display: flex;
    justify-content: center;
    align-items: center;
    gap: 14px;
  }
  .brand-dot {
    width: 44px; height: 44px;
    border-radius: 50%;
    background: var(--brand);
  }
  .brand-name {
    font-weight: 700;
    font-size: 32px;
    color: var(--brand);
    letter-spacing: 0.5px;
  }
  .headline {
    position: absolute;
    top: 122px;
    left: 28px; right: 28px;
    font-weight: 800;
    font-size: 42px;
    line-height: 56px;
  }
  .subhead {
    position: absolute;
    top: 322px;
    left: 30px; right: 30px;
    font-weight: 500;
    font-size: 26px;
    line-height: 38px;
  }
  .portrait {
    position: absolute;
    top: 405px;
    left: 170px;
    width: 443px;
    height: 418px;
  }
  .offer {
    position: absolute;
    top: 836px;
    left: 20px; right: 20px;
    font-weight: 700;
    font-size: 33px;
    line-height: 46px;
  }
  .cta {
    position: absolute;
    top: 962px;
    left: 73px;
    width: 637px;
    height: 88px;
    display: flex;
    align-items: center;
    justify-content: center;
    background: var(--button);
    box-shadow: 0 4px 0 var(--button-shadow);
    border-radius: 6px;
    color: var(--white);
    font-weight: 700;
    font-size: 28px;
    text-decoration: none;
    text-transform: uppercase;
  }
  .fine-print {
    position: absolute;
    top: 1108px;
    left: 0; right: 0;
    font-weight: 500;
    font-size: 26px;
  }
</style>
</head>
<body>
<main class="banner">
  <header class="brand">
    <span class="brand-dot"></span>
    <span class="brand-name">Brightlane Promotion Hub</span>
  </header>

  <h1 class="headline">Are You Ready To Commit To Taking Your Business To The Next Level?</h1>
  <p class="subhead">Because We're In This For The Long-Haul and Dedicated To Your Success...</p>

  <svg class="portrait" viewBox="0 30 412 432" preserveAspectRatio="none" xmlns="http://www.w3.org/2000/svg">
    <defs>
      <linearGradient id="portrait-fill" x1="0" y1="0" x2="0" y2="1">
        <stop offset="0" stop-color="var(--photo-light)"/>
        <stop offset="0.55" stop-color="var(--photo-mid)"/>
        <stop offset="1" stop-color="var(--photo-dark)"/>
      </linearGradient>
    </defs>
    <path role="img" aria-label="Photo of a confident businessman in a navy suit adjusting his tie"
          d="M206 440 C120 380 30 320 30 200 C30 110 90 55 150 55 C180 55 200 75 206 95 C212 75 232 55 262 55 C322 55 382 110 382 200 C382 320 292 380 206 440 Z"
          fill="url(#portrait-fill)"/>
    <path class="portrait-frame"
          d="M206 455 C110 390 14 325 14 198 C14 100 82 38 150 38 C178 38 198 52 206 70 C214 52 234 38 262 38 C330 38 398 100 398 198 C398 325 302 390 206 455 Z"
          fill="none" stroke="var(--frame)" stroke-width="3" stroke-dasharray="10 7"/>
  </svg>

  <p class="offer">Save $300 By Upgrading To An Annual Membership And Pay Only $74/mth</p>

  <a class="cta" href="https://tlpx.pagevault-example.com/page/tlp-annual-upsell">Yes, Upgrade My Plan Right Now!</a>

  <p class="fine-print">Must prepay the full year at only $898/yr!</p>
</main>
</body>
</html>
```